Nordisk Boligkontor

Company is in: Denmark - Copenhagen
It sells: Restaurants and café buildings
Companys age: 25 years
Main benefit: trust with over 25 years experience

```html
<!DOCTYPE html>
<html lang="en">
<head>
<meta charset="utf-8">
<title>Nordisk Boligkontor</title>
<link rel="stylesheet" href="https://fonts.googleapis.com/css2?family=Libre+Baskerville:wght@700&family=Arimo:ital,wght@0,400;0,700;1,400;1,700&display=swap">
<style>
  :root{
    --bg-deep:#250510;
    --bg-wine:#3b0a18;
    --stage:#330712;
    --nav:#7c0b2e;
    --nav-dark:#4b0619;
    --nav-line:#5a0820;
    --crimson:#7a0a2a;
    --cream:#f3e4bf;
    --cream-light:#f8f1e2;
    --panel:#f5e9cb;
    --panel-border:#d9c28f;
    --navy:#1c3a6b;
    --ink:#2a2320;
    --white:#ffffff;
  }
  *{box-sizing:border-box;margin:0;padding:0}
  html,body{width:1200px;height:900px;overflow:hidden}
  body{
    position:relative;
    font-family:"Arimo",Arial,sans-serif;
    color:var(--ink);
    background:linear-gradient(90deg,var(--bg-deep) 0%,var(--bg-wine) 30%,var(--bg-wine) 70%,var(--bg-deep) 100%);
  }
  .logo{
    position:absolute;left:116px;top:32px;
    font-family:"Libre Baskerville",Georgia,serif;font-weight:700;
    font-size:28px;color:var(--white);letter-spacing:0.5px;
  }
  .search{position:absolute;left:798px;top:22px;display:flex;gap:4px}
  .search-field{
    width:212px;height:32px;background:var(--white);border:2px solid #c9b6b6;
    font-size:13px;color:#777;padding:7px 10px;
  }
  .search-button{width:36px;height:32px;background:var(--crimson);display:flex;align-items:center;justify-content:center}
  .advanced{
    position:absolute;right:152px;top:64px;font-size:14px;color:var(--white);text-decoration:underline;
  }
  .nav{
    position:absolute;left:114px;top:100px;width:978px;height:58px;
    background:linear-gradient(var(--nav),#6a0926);display:flex;
  }
  .nav a{
    display:flex;align-items:center;justify-content:center;height:100%;
    color:var(--white);font-weight:700;font-size:18px;text-decoration:none;
    border-right:2px solid var(--nav-line);
  }
  .nav a:last-child{border-right:none}
  .nav .current{background:var(--nav-dark)}
  .stage{position:absolute;left:114px;top:158px;width:978px;height:352px;background:var(--stage)}
  .slider{
    position:absolute;left:136px;top:188px;width:638px;height:296px;
    background:linear-gradient(100deg,#4a3424 0%,#c9a576 22%,#8a6238 45%,#d8c39a 62%,#5a3a26 80%,#2e2018 100%);
  }
  .slider-arrow{position:absolute;top:318px}
  .pager{position:absolute;left:628px;top:448px;display:flex;gap:2px}
  .pager span{
    width:20px;height:22px;background:#d9d2cc;color:var(--ink);font-size:12px;
    display:flex;align-items:center;justify-content:center;
  }
  .pager .active{background:var(--crimson);color:var(--white)}
  .box{
    position:absolute;left:808px;width:258px;background:var(--panel);
    border:3px solid var(--panel-border);padding:10px 12px;
  }
  .box-title{font-style:italic;color:var(--navy);font-size:17px;margin-bottom:8px}
  .box-title strong{font-style:normal}
  .box p{font-size:14px;line-height:20px;color:var(--ink)}
  .box-newsletter p{font-style:italic}
  .button{
    position:absolute;background:var(--crimson);color:var(--white);font-weight:700;font-size:13px;
    display:flex;align-items:center;justify-content:center;border:1px solid #b06a80;
  }
  .email-field{
    position:absolute;left:12px;top:88px;width:198px;height:30px;background:var(--white);
    border:2px solid var(--panel-border);font-size:12px;color:#888;padding:6px 10px;font-style:italic;
  }
  .welcome{
    position:absolute;left:114px;top:510px;width:978px;height:190px;background:var(--cream);
    padding:14px 40px 0 36px;
  }
  .welcome h1{font-size:27px;color:var(--navy);font-weight:700;margin-bottom:8px}
  .welcome p{font-size:15.5px;line-height:25px;color:var(--ink)}
  .venues{
    position:absolute;left:114px;top:700px;width:978px;height:200px;background:var(--cream-light);
  }
  .venue{position:absolute;top:0;width:262px}
  .venue h2{font-size:27px;color:var(--crimson);font-weight:700;margin:20px 0 12px 0}
  .venue-photo{
    width:262px;height:130px;border:4px solid var(--white);box-shadow:0 2px 6px rgba(0,0,0,.35);
  }
  .venue p{font-size:14px;line-height:20px;margin-top:10px}
</style>
</head>
<body>
  <div class="logo">NORDISK BOLIGKONTOR</div>

  <div class="search">
    <div class="search-field">Search...</div>
    <div class="search-button">
      <svg width="16" height="16" viewBox="0 0 16 16"><circle cx="6.5" cy="6.5" r="4.5" fill="none" stroke="#fff" stroke-width="2"/><line x1="10" y1="10" x2="14" y2="14" stroke="#fff" stroke-width="2"/></svg>
    </div>
  </div>
  <a class="advanced">Advanced search</a>

  <nav class="nav">
    <a class="current" style="width:120px">Home</a>
    <a style="width:142px">For Sale</a>
    <a style="width:226px">Links/Download</a>
    <a style="width:168px">Newsletter</a>
    <a style="width:160px">About Us</a>
    <a style="width:162px">Contact Us</a>
  </nav>

  <div class="stage"></div>
  <div class="slider" role="img" aria-label="Photo of an elegant restaurant dining room with open kitchen"></div>
  <svg class="slider-arrow" style="left:158px" width="28" height="40" viewBox="0 0 28 40"><polygon points="24,2 4,20 24,38 24,28 14,20 24,12" fill="#7a0a2a"/></svg>
  <svg class="slider-arrow" style="left:722px" width="28" height="40" viewBox="0 0 28 40"><polygon points="4,2 24,20 4,38 4,28 14,20 4,12" fill="#9a9a9a"/></svg>
  <div class="pager"><span class="active">1</span><span>2</span><span>3</span><span>4</span><span>5</span><span>6</span></div>

  <div class="box box-question" style="top:188px;height:132px">
    <div class="box-title">Have a question?</div>
    <p>Lorem ipsum dolor sit amet, consectetuer adipiscing elit.</p>
    <div class="button" style="left:140px;top:92px;width:104px;height:28px">Go to form</div>
  </div>

  <div class="box box-newsletter" style="top:348px;height:136px">
    <div class="box-title">Get our <strong>NEWSLETTER</strong></div>
    <p>Enter your email address if you want to receive our newsletter</p>
    <div class="email-field">e-mail</div>
    <div class="button" style="left:212px;top:88px;width:32px;height:30px">Go</div>
  </div>

  <section class="welcome">
    <h1>Welcome to NORDISK BOLIGKONTOR</h1>
    <p>Lorem ipsum dolor sit amet, consectetuer adipiscing elit. Aenean commodo ligula eget dolor. Aenean massa. Cum sociis natoque penatibus et magnis dis parturient montes, nascetur ridiculus mus. Donec quam felis, ultricies nec, pellentesque eu, pretium quis, sem. Nulla consequat massa quis enim. Donec pede justo, fringilla vel, aliquet nec, vulputate eget, arcu. In enim justo, rhoncus ut, imperdiet a, venenatis vitae, justo. Nullam dictum felis eu pede mollis pretium. Integer tincidunt. Cras dapibus. Vivamus elementum semper nisi.</p>
  </section>

  <section class="venues">
    <div class="venue" style="left:38px">
      <h2>Restaurant</h2>
      <div class="venue-photo" role="img" aria-label="Photo of a restaurant interior in purple light" style="background:linear-gradient(135deg,#3a2a5a,#8a6ab0 45%,#d8cfe0 70%,#4a3a60)"></div>
      <p>Lorem ipsum dolor sit</p>
    </div>
    <div class="venue" style="left:358px">
      <h2>Cafe</h2>
      <div class="venue-photo" role="img" aria-label="Photo of a cafe table setting in warm golden tones" style="background:linear-gradient(135deg,#a8701c,#e0b64a 45%,#f2e2b0 70%,#b88a3a)"></div>
      <p>Lorem ipsum dolor sit</p>
    </div>
    <div class="venue" style="left:682px">
      <h2>Pab</h2>
      <div class="venue-photo" role="img" aria-label="Photo of a traditional pub facade on a street corner" style="background:linear-gradient(180deg,#c8ccd4,#8a6a4a 40%,#4a2a1e 75%,#2a2a2a)"></div>
      <p>Lorem ipsum dolor sit</p>
    </div>
  </section>
</body>
</html>
```